Create banner ads for a digital product that deletes personal information from the web

The context of the banners is general advertisement for our service.
Please provide us with a set of static and flash/gif banners in the following standard sizes for the theme you create:
160x600
300x250
300x600
320x250
336x280
728x90
Please see our website for logo (just our name) and theme ideas - please follow similar color/font schemes if possible. www.quillbarrow.com
Our company is an online service that deletes personal information from the internet for our members (automated opt-outs and content removal). Our target audience is anyone who wishes to protect their personal information from being on the internet (i.e. prefer to fly under the internet radar, for example). This is a product for U.S. residents who value privacy and online reputation. We seek to provide members with control of what 300+ websites are sharing about them – removing names, addresses, ages, phone numbers, email addresses, children’s information, home/property value information etc.

```html
<!DOCTYPE html>
<html lang="en">
<head>
<meta charset="utf-8">
<title>Quillbarrow banner set</title>
<link rel="stylesheet" href="https://fonts.googleapis.com/css2?family=PT+Sans:wght@400;700&display=swap">
<style>
  :root {
    --canvas: #ffffff;
    --paper-light: #f4f4f4;
    --paper-mid: #e6e6e6;
    --frame: #4a4a4a;
    --ink: #1c1c1c;
    --button-top: #5a9a1c;
    --button-bottom: #2f6a08;
    --button-edge: #24500a;
    --button-text: #ffffff;
    --art-dark: #3a3a3a;
    --art-light: #dcdcdc;
  }
  * { box-sizing: border-box; margin: 0; padding: 0; }
  html, body { width: 1200px; height: 610px; overflow: hidden; background: var(--canvas); }
  body { position: relative; font-family: "PT Sans", Arial, sans-serif; color: var(--ink); }

  .banner {
    position: absolute;
    border: 1px solid var(--frame);
    background: radial-gradient(ellipse at 40% 35%, var(--paper-light), var(--paper-mid));
    overflow: hidden;
  }
  .banner > * { position: absolute; }

  .brand { font-weight: 400; white-space: nowrap; left: 0; right: 0; text-align: center; line-height: 1; }
  .headline { font-weight: 700; text-transform: uppercase; text-align: center; left: 0; right: 0; }
  .artwork {
    border-radius: 8px;
    background: linear-gradient(135deg, var(--art-dark) 0%, var(--art-dark) 48%, var(--art-light) 52%, #f2f2f2 100%);
    opacity: .85;
  }
  .cta {
    display: flex; align-items: center; justify-content: center; text-align: center;
    background: linear-gradient(var(--button-top), var(--button-bottom));
    border: 1px solid var(--button-edge);
    border-radius: 6px;
    color: var(--button-text);
    font-weight: 700; text-transform: uppercase;
    box-shadow: 0 2px 3px rgba(0,0,0,.35);
  }

  /* 300x600 */
  .skyscraper-wide { left: 6px; top: 6px; width: 300px; height: 601px; }
  .skyscraper-wide .brand { top: 62px; font-size: 32px; }
  .skyscraper-wide .headline { top: 184px; font-size: 22px; line-height: 29px; }
  .skyscraper-wide .artwork { left: 50px; top: 360px; width: 200px; height: 115px; }
  .skyscraper-wide .cta { left: 34px; top: 530px; width: 230px; height: 39px; font-size: 17px; }

  /* 160x600 */
  .skyscraper { left: 307px; top: 6px; width: 161px; height: 601px; }
  .skyscraper .brand { top: 66px; font-size: 22px; }
  .skyscraper .headline { top: 170px; font-size: 18px; line-height: 24px; }
  .skyscraper .artwork { left: 3px; top: 364px; width: 152px; height: 85px; }
  .skyscraper .cta { left: 4px; top: 503px; width: 152px; height: 55px; font-size: 16px; line-height: 21px; }

  /* 728x90 */
  .leaderboard { left: 470px; top: 6px; width: 729px; height: 91px; }
  .leaderboard .brand { left: 22px; right: auto; top: 30px; font-size: 28px; }
  .leaderboard .headline { left: 200px; right: auto; width: 220px; top: 14px; font-size: 16px; line-height: 20px; font-weight: 700; }
  .leaderboard .artwork { left: 420px; top: 2px; width: 130px; height: 86px; }
  .leaderboard .cta { left: 557px; top: 17px; width: 152px; height: 54px; font-size: 16px; line-height: 20px; }

  /* 320x250 */
  .rectangle-wide { left: 470px; top: 101px; width: 320px; height: 250px; }
  .rectangle-wide .brand { top: 14px; font-size: 24px; }
  .rectangle-wide .headline { top: 51px; font-size: 15.5px; line-height: 20px; }
  .rectangle-wide .artwork { left: 66px; top: 97px; width: 203px; height: 98px; }
  .rectangle-wide .cta { left: 44px; top: 200px; width: 230px; height: 40px; font-size: 16px; }

  /* 336x280 */
  .rectangle-large { left: 795px; top: 101px; width: 336px; height: 280px; }
  .rectangle-large .brand { top: 20px; font-size: 26px; }
  .rectangle-large .headline { top: 62px; font-size: 17px; line-height: 20px; }
  .rectangle-large .artwork { left: 66px; top: 111px; width: 220px; height: 108px; }
  .rectangle-large .cta { left: 42px; top: 224px; width: 249px; height: 42px; font-size: 17px; }

  /* 300x250 */
  .rectangle { left: 470px; top: 356px; width: 300px; height: 250px; }
  .rectangle .brand { top: 13px; font-size: 24px; }
  .rectangle .headline { top: 50px; font-size: 15.5px; line-height: 20px; }
  .rectangle .artwork { left: 56px; top: 96px; width: 210px; height: 97px; }
  .rectangle .cta { left: 36px; top: 201px; width: 229px; height: 39px; font-size: 16px; }
</style>
</head>
<body>

<section class="banner skyscraper-wide" aria-label="300 by 600 banner">
  <div class="brand">Quillbarrow</div>
  <h2 class="headline">Removing<br>your personal<br>information from<br>the internet</h2>
  <div class="artwork" role="img" aria-label="Illustration of a personal ID card beside a keyboard Delete key"></div>
  <div class="cta">Protect my privacy now</div>
</section>

<section class="banner skyscraper" aria-label="160 by 600 banner">
  <div class="brand">Quillbarrow</div>
  <h2 class="headline">Removing<br>your personal<br>information<br>from the<br>internet</h2>
  <div class="artwork" role="img" aria-label="Illustration of a personal ID card beside a keyboard Delete key"></div>
  <div class="cta">Protect<br>my privacy now</div>
</section>

<section class="banner leaderboard" aria-label="728 by 90 banner">
  <div class="brand">Quillbarrow</div>
  <h2 class="headline">Removing your personal information from the internet</h2>
  <div class="artwork" role="img" aria-label="Illustration of a personal ID card beside a keyboard Delete key"></div>
  <div class="cta">Protect<br>my privacy now</div>
</section>

<section class="banner rectangle-wide" aria-label="320 by 250 banner">
  <div class="brand">Quillbarrow</div>
  <h2 class="headline">Removing your personal<br>information from the internet</h2>
  <div class="artwork" role="img" aria-label="Illustration of a personal ID card beside a keyboard Delete key"></div>
  <div class="cta">Protect my privacy now</div>
</section>

<section class="banner rectangle-large" aria-label="336 by 280 banner">
  <div class="brand">Quillbarrow</div>
  <h2 class="headline">Removing your personal<br>information from the internet</h2>
  <div class="artwork" role="img" aria-label="Illustration of a personal ID card beside a keyboard Delete key"></div>
  <div class="cta">Protect my privacy now</div>
</section>

<section class="banner rectangle" aria-label="300 by 250 banner">
  <div class="brand">Quillbarrow</div>
  <h2 class="headline">Removing your personal<br>information from the internet</h2>
  <div class="artwork" role="img" aria-label="Illustration of a personal ID card beside a keyboard Delete key"></div>
  <div class="cta">Protect my privacy now</div>
</section>

</body>
</html>
```